New look and feel for a Website, mobile design, desktop design

We do a redesign of the website quonbath.com. We expect the designer to come up with ideas about a new look AND feel.
Starting point of the designers considerations should be the mobile design. Even though we are not creating a mobile App, the designer should think of it as one regarding design and usability. Using responsive design technology, we will shift from the mobile design to the desktop design and likewise. So the designer is supposed to come up with a solution for that as well.
What we expect
- definition of single design-elements that can be used in various places
- creation of a mobile design for all different types of pages
- creation of a desktop design for all different types of pages
Find a detailed description in the redesign-specification.

Target Market(s)

Germany, Austria, Switzerland

Industry/Entity Type

Residential Construction

Number of Pages Required

5+ page

Font styles to use
Other font styles liked:
• Open Sans

Colors

Designer to choose colors to be used in the design.

Requirements
Must have
• - mobile design concept
• - desktop design concept

```html
<!DOCTYPE html>
<html lang="de">
<head>
<meta charset="utf-8">
<title>quonbath – Ein neues Bad in 24 Stunden</title>
<link rel="stylesheet" href="https://fonts.googleapis.com/css2?family=Open+Sans:wght@400;600;700;800&display=swap">
<style>
:root{
  --navy:#0b4a6e;
  --blue:#1590d6;
  --ink:#3a3f45;
  --muted:#6b7076;
  --slate:#4a5058;
  --orange:#f07c1b;
  --line:#dcdfe2;
  --footer:#333537;
  --footer-deep:#262829;
  --white:#ffffff;
}
*{box-sizing:border-box;margin:0;padding:0}
html,body{width:1200px;height:2239px;overflow:hidden}
body{font-family:"Open Sans",Arial,sans-serif;color:var(--ink);background:var(--white);position:relative}
.abs{position:absolute}

/* top bar */
.topbar{left:0;top:0;width:1200px;height:39px;background:var(--navy);color:var(--white);font-size:12px;font-weight:600}
.topbar .contact{left:160px;top:0;height:39px;display:flex;align-items:center;gap:18px}
.topbar .contact span{display:flex;align-items:center;gap:7px}
.flag{width:22px;height:13px;display:block}
.topbar .cta{right:160px;top:0;height:39px;display:flex}
.cta a{display:flex;align-items:center;justify-content:center;height:39px;text-decoration:none;font-size:12px;font-weight:700}
.cta .consult{width:176px;background:var(--white);color:var(--navy)}
.cta .request{width:81px;background:var(--blue);color:var(--white)}

/* navigation */
.nav{left:0;top:39px;width:1200px;height:85px;background:var(--white)}
.brand{left:160px;top:20px;display:flex;flex-direction:column;align-items:center;gap:4px}
.brand .dot{width:30px;height:30px;border-radius:50%;background:var(--blue)}
.brand .name{font-size:22px;font-weight:700;color:var(--navy);line-height:1}
.menu{right:160px;top:0;height:85px;display:flex;gap:27px;list-style:none}
.menu li{height:85px;display:flex;align-items:center;font-size:13px;color:#8a8f95;position:relative}
.menu li.active{color:var(--blue);font-weight:600}
.menu li.active::after{content:"";position:absolute;left:0;right:0;bottom:0;height:3px;background:var(--blue)}

/* hero */
.hero{left:0;top:124px;width:1200px;height:512px;background:linear-gradient(100deg,#8e9396 0%,#b8bcbe 35%,#cfd2d2 60%,#a9adb0 100%)}
.hero h1{left:160px;top:120px;width:520px;font-size:46px;font-weight:800;line-height:56px;color:var(--white);letter-spacing:.5px}
.hero p{left:160px;top:250px;width:320px;font-size:18px;font-weight:600;line-height:22px;color:var(--white)}
.hero .btn-ghost{left:160px;top:327px;width:149px;height:55px;border:2px solid var(--white);color:var(--white);font-size:15px;font-weight:600;display:flex;align-items:center;justify-content:center}

/* welcome */
.welcome h2{left:160px;top:683px;font-size:46px;font-weight:800;line-height:52px;color:var(--navy)}
.welcome .tag{left:160px;top:798px;font-size:19px;font-weight:600;color:var(--ink)}
.welcome h3{left:475px;top:688px;font-size:14px;font-weight:700;color:var(--ink)}
.welcome .lead{left:475px;top:714px;width:555px;font-size:12px;line-height:18px;color:var(--muted)}
.btn-dark{background:var(--slate);color:var(--white);font-weight:700;display:flex;align-items:center;justify-content:center;border-radius:3px}
.welcome .btn-dark{left:475px;top:767px;width:207px;height:49px;font-size:13px}
.divider{left:160px;top:865px;width:880px;height:1px;background:var(--line)}

/* service badges */
.badges{left:160px;top:890px;width:880px;display:flex;justify-content:space-between}
.badge{width:240px;display:flex;flex-direction:column;align-items:center}
.badge .mark{width:150px;height:62px;border:3px solid var(--orange);border-radius:6px;background:#fff6ee}
.badge p{margin-top:9px;font-size:11.5px;font-weight:600;line-height:16px;text-align:center;color:#222}

/* services band */
.band{left:0;top:1054px;width:1200px;height:506px;background:var(--navy)}
.band h2{left:0;top:52px;width:1200px;text-align:center;font-size:32px;font-weight:800;color:var(--white)}
.cards{left:160px;top:112px;width:880px;display:flex;justify-content:space-between}
.card{width:271px;height:332px;background:var(--white);position:relative}
.card .photo{height:156px}
.card h3{position:absolute;left:23px;top:180px;width:230px;font-size:15px;font-weight:700;line-height:18px;color:var(--ink)}
.card.primary h3{color:var(--blue)}
.card p{position:absolute;left:23px;top:228px;width:230px;font-size:11.5px;line-height:16px;color:var(--muted)}
.card .btn{position:absolute;left:23px;top:273px;width:139px;height:31px;font-size:10px;font-weight:700;color:var(--white);background:var(--slate);border-radius:3px;display:flex;align-items:center;justify-content:center}
.card.primary .btn{background:var(--blue)}

/* references */
.refs h2{left:0;top:1604px;width:1200px;text-align:center;font-size:27px;font-weight:700;color:var(--ink)}
.gallery{left:160px;top:1669px;width:880px;height:177px;display:flex}
.gallery .tile{flex:1;position:relative}
.tile .overlay{position:absolute;inset:0;background:rgba(20,22,24,.55);display:flex;flex-direction:column;align-items:center;justify-content:center;gap:12px;color:var(--white);font-size:13px;font-weight:700}
.pager{left:565px;top:1880px;display:flex;gap:10px}
.pager span{width:28px;height:28px;border:1px solid #bbb;border-radius:3px;font-size:13px;font-weight:700;display:flex;align-items:center;justify-content:center}
.pager .current{background:var(--slate);border-color:var(--slate);color:var(--white)}

/* footer */
.footer{left:0;top:1964px;width:1200px;height:224px;background:var(--footer);color:#c9cbcd}
.footer .brand{left:160px;top:12px}
.footer .brand .name{color:var(--white);font-size:28px}
.footer .brand .dot{width:40px;height:40px}
.footer .about{left:160px;top:112px;width:395px;font-size:10px;line-height:14px;color:#b4b7ba}
.footer h4{font-size:15px;font-weight:600;color:var(--white)}
.quick{left:594px;top:22px}
.quick ul{list-style:none;margin-top:10px}
.quick li{font-size:10px;line-height:19.4px;padding-left:30px;position:relative}
.quick li::before{content:"›";position:absolute;left:14px;color:var(--blue);font-size:13px;line-height:19px}
.contactus{left:772px;top:22px}
.contactus ul{list-style:none;margin-top:8px}
.contactus li{font-size:10px;line-height:24px;display:flex;align-items:center;gap:12px}
.contactus svg{width:12px;height:12px}
.social{left:795px;top:157px;display:flex;gap:6px}
.social span{width:26px;height:26px;border-radius:50%;background:var(--white);display:block}
.bottombar{left:0;top:2188px;width:1200px;height:51px;background:var(--footer-deep);color:#b4b7ba;font-size:10px}
.bottombar .legal{left:160px;top:19px}
.bottombar .copy{right:160px;top:19px}
.quickquery{left:1049px;top:2203px;width:129px;height:36px;background:var(--blue);border-radius:6px 6px 0 0;color:var(--white);font-size:11px;font-weight:700;display:flex;align-items:center;justify-content:center;gap:7px}
</style>
</head>
<body>

<header class="abs topbar">
  <div class="abs contact">
    <span>
      <svg width="12" height="12" viewBox="0 0 12 12"><path d="M2.5 1l2 2-1 1.5a7 7 0 0 0 4 4L9 7.5l2 2L9.5 11A9 9 0 0 1 1 2.5z" fill="#fff"/></svg>
      <svg class="flag" viewBox="0 0 22 13"><rect width="22" height="13" fill="#ed2939"/><rect y="4.3" width="22" height="4.4" fill="#fff"/></svg>
      0800 11 22 33
    </span>
    <span>
      <svg class="flag" viewBox="0 0 22 13"><rect width="22" height="4.4" fill="#000"/><rect y="4.3" width="22" height="4.4" fill="#dd0000"/><rect y="8.7" width="22" height="4.3" fill="#ffce00"/></svg>
      0800 44 55 666
    </span>
    <span>
      <svg class="flag" viewBox="0 0 22 13"><rect width="22" height="13" fill="#d52b1e"/><rect x="9.5" y="2.5" width="3" height="8" fill="#fff"/><rect x="7" y="5" width="8" height="3" fill="#fff"/></svg>
      0800 77 88 99
    </span>
    <span>
      <svg width="16" height="12" viewBox="0 0 16 12"><rect x="1" y="1" width="14" height="10" fill="none" stroke="#fff" stroke-width="1.5"/><path d="M1 1l7 6 7-6" fill="none" stroke="#fff" stroke-width="1.5"/></svg>
      info@quonbath.com
    </span>
  </div>
  <div class="abs cta">
    <a class="consult" href="#">kostenlose Badberatung</a>
    <a class="request" href="#">Anfrage</a>
  </div>
</header>

<nav class="abs nav">
  <div class="abs brand"><span class="dot"></span><span class="name">quonbath</span></div>
  <ul class="abs menu">
    <li class="active">Badlösungen</li>
    <li>Badinformationen</li>
    <li>Messen</li>
    <li>Kundenmeinungen</li>
    <li>Standorte</li>
    <li>Presse</li>
    <li>Über quonbath</li>
  </ul>
</nav>

<section class="abs hero" role="img" aria-label="Helles Badezimmer mit Marmorwänden, freistehender Badewanne und bodengleicher Glasdusche">
  <h1 class="abs">EIN NEUES BAD IN 24 STUNDEN</h1>
  <p class="abs">mit quonbath Systemlösungen zur Badrenovierung</p>
  <a class="abs btn-ghost">READ MORE</a>
</section>

<section class="welcome">
  <h2 class="abs">Welcome<br>To Quonbath</h2>
  <p class="abs tag">Ein neues Bad in 24 Stunden</p>
  <h3 class="abs">24h Badrenovierung</h3>
  <p class="abs lead">quonbath hat sich auf hochqualitative Badsanierungen spezialisiert, bei denen Sie nach nur 24 Stunden in Ihre neue, barrierefreie Dusche steigen.</p>
  <a class="abs btn-dark">BAD INFORMATIONEN</a>
</section>

<div class="abs divider"></div>

<section class="abs badges">
  <div class="badge">
    <div class="mark" role="img" aria-label="Produktsiegel 3h Fugensanierung"></div>
    <p>Wanne raus, Dusche rein! Oder einfach nur<br>eine neue Dusche innerhalb eines Tages!</p>
  </div>
  <div class="badge">
    <div class="mark" role="img" aria-label="Produktsiegel 8h Duschrenovierung"></div>
    <p>Wanne raus, Dusche rein! Oder einfach nur<br>eine neue Dusche innerhalb eines Tages!</p>
  </div>
  <div class="badge">
    <div class="mark" role="img" aria-label="Produktsiegel 24h Badrenovierung"></div>
    <p>Ein neues Bad, barrierefrei und senioren-<br>gerecht! Und das innerhalb von 24 Arbeitss-</p>
  </div>
</section>

<section class="abs band">
  <h2 class="abs">BEDARFSGERECHTER BADUMBAU</h2>
  <div class="abs cards">
    <article class="card primary">
      <div class="photo" role="img" aria-label="Moderne Dusche mit grünlicher Glaswand und Holzelementen" style="background:linear-gradient(90deg,#b98d62,#c9d6c3 45%,#e6e2da)"></div>
      <h3>Badausstattung für Ihr neues Bad</h3>
      <p>Die optimale Badausstattung berücksich-tigt den Wunsch nach stetig steigendem</p>
      <a class="btn">BAD INFORMATIONEN</a>
    </article>
    <article class="card">
      <div class="photo" role="img" aria-label="Komplettbad mit dunkelroter Wand, Waschtisch und Haltegriffen" style="background:linear-gradient(90deg,#d9d8d6,#a8a4a2 40%,#7a2630 65%,#d4d2cf)"></div>
      <h3>Das Komplettbad in 24 Stunden</h3>
      <p>In lediglich drei Arbeitstagen oder besser:<br>In nur 24 Arbeitsstunden entsteht Ihr.</p>
      <a class="btn">BAD INFORMATIONEN</a>
    </article>
    <article class="card">
      <div class="photo" role="img" aria-label="Badplaner berät ein älteres Paar am Esstisch zu Hause" style="background:linear-gradient(90deg,#b49b7c,#6f8fae 50%,#cbb8a0)"></div>
      <h3>Der Badplaner, der zu Ihnen nach Hause kommt</h3>
      <p>Sparen Sie Zeit und lassen Sie sich zuhause beraten! Die quonbath Badplaner.</p>
      <a class="btn">BAD INFORMATIONEN</a>
    </article>
  </div>
</section>

<section class="refs">
  <h2 class="abs">Empfehlungen | Übersicht</h2>
  <div class="abs gallery">
    <div class="tile" role="img" aria-label="Helles Bad mit Glasdusche und Waschtisch" style="background:linear-gradient(90deg,#e4e4e2,#cfd3d4 60%,#b9bec0)"></div>
    <div class="tile" role="img" aria-label="Komplettbad mit dunkelroter Wand" style="background:linear-gradient(90deg,#c9c7c5,#8d2a33 60%,#d0cdca)">
      <div class="overlay">
        <svg width="24" height="24" viewBox="0 0 24 24"><circle cx="10" cy="10" r="7" fill="none" stroke="#fff" stroke-width="2.5"/><path d="M15 15l6 6" stroke="#fff" stroke-width="3" stroke-linecap="round"/><path d="M7 10h6M10 7v6" stroke="#fff" stroke-width="2"/></svg>
        Das Komplettbad in 24 Stunden
      </div>
    </div>
    <div class="tile" role="img" aria-label="Badewanne mit orangefarbenem Band vor heller Wand" style="background:linear-gradient(90deg,#d6d3cd,#c7c3bc 60%,#e9a26a 85%,#d8d4ce)"></div>
  </div>
  <div class="abs pager"><span class="current">1</span><span>2</span></div>
</section>

<footer class="abs footer">
  <div class="abs brand"><span class="dot"></span><span class="name">quonbath</span></div>
  <p class="abs about">Die Badsanierung mit quonbath ist einfacher und unkomplizierter als Sie vielleicht denken. Mit uns renovieren Sie ohne viel Schmutz und Lärm und völlig unkompliziert, denn Sie haben nur einen Ansprechpartner.<br><br>der sich für Sie um alles kümmert.</p>
  <div class="abs quick">
    <h4>Quick Links</h4>
    <ul>
      <li>Badlösungen</li><li>Badinformationen</li><li>Messen</li><li>Kundenmeinungen</li><li>Standorte</li><li>Presse</li><li>Über quonbath</li>
    </ul>
  </div>
  <div class="abs contactus">
    <h4>Contact Us</h4>
    <ul>
      <li><svg viewBox="0 0 12 12"><path d="M6 1a3.5 3.5 0 0 1 3.5 3.5C9.5 7 6 11 6 11S2.5 7 2.5 4.5A3.5 3.5 0 0 1 6 1z" fill="#9a9da0"/></svg>Lorem ipsum dolor sit amet, consectetur adipiscin</li>
      <li><svg viewBox="0 0 12 12"><path d="M2.5 1l2 2-1 1.5a7 7 0 0 0 4 4L9 7.5l2 2L9.5 11A9 9 0 0 1 1 2.5z" fill="#9a9da0"/></svg>Phone:00 1234 5678</li>
      <li><svg viewBox="0 0 12 12"><rect x="1" y="4" width="10" height="6" fill="#9a9da0"/><rect x="3" y="1" width="6" height="3" fill="#9a9da0"/></svg>Fax:00 1234 5678</li>
      <li><svg viewBox="0 0 12 12"><rect x="1" y="2" width="10" height="8" fill="#9a9da0"/><path d="M1 2l5 4 5-4" fill="none" stroke="#333" stroke-width="1"/></svg>Email: quonbath.com</li>
    </ul>
  </div>
  <div class="abs social" aria-label="Soziale Netzwerke">
    <span></span><span></span><span></span><span></span><span></span>
  </div>
</footer>

<div class="abs bottombar">
  <p class="abs legal">Privacy Policy | Terms &amp; Conditions</p>
  <p class="abs copy">©2018 Quonbath. Allrights are Reserved.</p>
</div>

<a class="abs quickquery">
  <svg width="16" height="14" viewBox="0 0 16 14"><path d="M1 1h14v9H6l-3 3v-3H1z" fill="none" stroke="#fff" stroke-width="1.5"/></svg>
  QUICK QUERY
</a>

</body>
</html>
```